" Window Blinds and Shutters Business Card Design"

We require a business card design for a new windows blinds and shutters company based in Sydney.
The business name is 'Larkvale Blinds and Shutters'.
We supply and install homes and businesses with internal and external window furnishings and finishes. This includes varieties of window blinds and window shutters.

Benefits of Larkvale Blinds and Shutters :
Added security and privacy,
The ability to control the amount of sunlight,
Regulate internal temperature.

Blinds varieties:
Roller Blinds, Double Roller Blinds, Roman Blinds, Vertical Blinds, Aluminium venetians, Timber venetians and PVC Venetians.

Shutters varieties:
Plantation Shutters, Aluminium Louvre Shutters, Roller Shutters and Security Shutters .
Updates

Hi Designers,

Please have a look at my Business card design brief. I need your help to start my new business.

Thanks,

Dorian.

Reason: not 100% happy with the options available, close to 90% happy, need a little more refinement. Thank You & Good Luck

Target Market(s)

Home owners, business owners, shift workers , and new home builders.

Industry/Entity Type

Security

Contact Information for Business Card

Larkvale Blinds and Shutters,

Dorian Kettlewell mobile: 0487561904,
Priya Hensworth mobile: 0472846015,

email: dorian.kettlewell@mailgrove.net
web: larkvaleblindsandshutters.com.au

Colors
ffffff
9d9d9d
f78f20

Requirements
Must have
• ON FRONT OF CARD
I have attached a picture of logo and need a designer to design a font logo for Larkvale Blinds and Shutters similar, or open to suggestions.

FRONT OF CARD
Company message/:
"Shaping light for every window"

BACK OF CARD
'For a FREE measure & quote call Dorian - 0487561904"
Nice to have
• Elegant yet professional.

Soft colours appealing to both male & female clients.

Should not have

• Unprofessional fonts

```html
<!DOCTYPE html>
<html lang="en">
<head>
<meta charset="utf-8">
<title>Larkvale Blinds and Shutters – Business Card</title>
<link rel="stylesheet" href="https://fonts.googleapis.com/css2?family=Open+Sans:wght@400;600&display=swap">
<style>
  :root {
    --orange: #f78f20;
    --orange-soft: #fbb469;
    --grey: #9d9d9d;
    --slate: #3b474c;
    --label: #8ea2a5;
    --paper: #ffffff;
  }
  * { margin: 0; padding: 0; box-sizing: border-box; }
  html, body {
    width: 1200px;
    height: 729px;
    overflow: hidden;
    background: var(--paper);
  }
  .card {
    position: relative;
    width: 1200px;
    height: 729px;
    background: var(--paper);
    font-family: "Open Sans", Arial, sans-serif;
    color: var(--slate);
  }
  .blind-art {
    position: absolute;
    left: 0;
    top: 0;
    width: 312px;
    height: 729px;
    background: linear-gradient(90deg, var(--orange) 0%, var(--orange) 30%, var(--orange-soft) 100%);
  }
  .brand-dot {
    position: absolute;
    left: 659px;
    top: 102px;
    width: 90px;
    height: 90px;
    border-radius: 50%;
    background: var(--grey);
  }
  .brand-name {
    position: absolute;
    left: 316px;
    top: 240px;
    width: 800px;
    text-align: center;
    font-size: 52px;
    line-height: 70px;
    font-weight: 600;
    color: var(--orange);
    white-space: nowrap;
  }
  .tagline {
    position: absolute;
    left: 377px;
    top: 312px;
    width: 700px;
    text-align: right;
    font-size: 37px;
    line-height: 50px;
    font-weight: 400;
    color: var(--slate);
    white-space: nowrap;
  }
  .contacts {
    position: absolute;
    left: 397px;
    top: 424px;
    width: 700px;
    text-align: center;
    font-size: 26px;
    line-height: 38px;
    color: var(--slate);
  }
  .contacts p { white-space: nowrap; }
  .contacts .gap { margin-top: 39px; }
  .contacts .web { margin-top: 41px; }
  .label { color: var(--label); }
</style>
</head>
<body>
  <main class="card">
    <div class="blind-art" role="img" aria-label="Orange venetian blind with slats and pull cord"></div>

    <div class="brand-dot"></div>
    <h1 class="brand-name">Larkvale Blinds and Shutters</h1>
    <p class="tagline">Shaping light for every window</p>

    <section class="contacts">
      <p>Dorian Kettlewell <span class="label">mobile: 0487561904</span></p>
      <p>Priya Hensworth <span class="label">mobile: 0472846015</span></p>
      <p class="gap"><span class="label">email:</span> dorian.kettlewell@mailgrove.net</p>
      <p class="web"><span class="label">web:</span> larkvaleblindsandshutters.com.au</p>
    </section>
  </main>
</body>
</html>
```